Lawn Sign For Construction Projects - Brisk Current

This contest is for a lawn sign that will be placed in the front yard of recently completed construction projects. The goal here is to have a bold advertising sign that is visible from a vehicle driving past.

We are still deciding on the default size for our sign, we also may use multiple sizes. The two sizes we will more than likely be using are: 18"h x 24"w and 24"h x 36"w.

Preference will be given to designers that submit original designs that tie into our current brand and are either in both the size formats listed above or are easy to scale in photoshop or illustrator.

In the files, you will see our logo and an example of a lawn sign.

Please contact us with any questions or comments you may have!

Thank You,
- The Brisk Current Team

Industry/Entity Type

Residential Construction

Colors
34a7d8
ffffff
faa54b

Requirements
Nice to have
• 1. The sign must tie into our current branding and color scheme.
• 2. The sign must be clearly visible and readable.
• 3. The sign must include our phone number in readable print.
• 4. Our website written in small print along the bottom of the sign.
• 5. Must mention we install the following products:
• a.) Solar
• b.) Roofing
• c.) Windows
• d.) Artificial Lawn
• e.) Whole House Fans
• f.) Patio Covers

```html
<!DOCTYPE html>
<html lang="en">
<head>
<meta charset="utf-8">
<title>Brisk Current Lawn Sign</title>
<link rel="stylesheet" href="https://fonts.googleapis.com/css2?family=Anton&family=Montserrat:wght@500;600;900&display=swap">
<style>
  :root {
    --backdrop: #e9ebe8;
    --sign-black: #000000;
    --sign-yellow: #fff200;
    --sign-blue: #1075bd;
    --brand-orange: #f06a23;
    --text-white: #ffffff;
  }
  html, body {
    margin: 0;
    padding: 0;
    width: 1200px;
    height: 1200px;
    overflow: hidden;
    background: var(--backdrop);
  }
  .canvas {
    position: relative;
    width: 1200px;
    height: 1200px;
  }
  .lawn-sign {
    position: absolute;
    left: 211px;
    top: 82px;
    width: 778px;
    height: 1036px;
    display: block;
  }
  .panel-top { fill: var(--sign-black); }
  .panel-bottom { fill: var(--sign-blue); }
  .arrow { fill: var(--sign-yellow); }
  .brand-mark { fill: var(--brand-orange); }
  .brand-name {
    font-family: "Montserrat", sans-serif;
    font-weight: 600;
    fill: var(--brand-orange);
  }
  .offer-amount {
    font-family: "Anton", sans-serif;
    fill: var(--brand-orange);
  }
  .offer-label {
    font-family: "Montserrat", sans-serif;
    font-weight: 900;
    fill: var(--brand-orange);
  }
  .phone {
    font-family: "Montserrat", sans-serif;
    font-weight: 500;
    fill: var(--text-white);
  }
  .website {
    font-family: "Montserrat", sans-serif;
    font-weight: 500;
    fill: var(--brand-orange);
  }
</style>
</head>
<body>
<main class="canvas">
  <svg class="lawn-sign" viewBox="0 0 778 1036" xmlns="http://www.w3.org/2000/svg" aria-label="Brisk Current lawn sign: $0 down">
    <rect class="panel-top" x="0" y="0" width="778" height="570"/>
    <rect class="panel-bottom" x="0" y="570" width="778" height="466"/>
    <polygon class="arrow" points="154,205 623,205 623,570 758,570 389,850 21,570 154,570"/>

    <g class="brand">
      <circle class="brand-mark" cx="150" cy="111" r="42"/>
      <text class="brand-name" x="218" y="132" font-size="54" textLength="525" lengthAdjust="spacingAndGlyphs">BRISK CURRENT</text>
    </g>

    <text class="offer-amount" x="381" y="536" font-size="340" text-anchor="middle" textLength="384" lengthAdjust="spacingAndGlyphs">$0</text>
    <text class="offer-label" x="389" y="662" font-size="116" text-anchor="middle" textLength="432" lengthAdjust="spacingAndGlyphs">DOWN</text>

    <text class="phone" x="389" y="946" font-size="104" text-anchor="middle" textLength="668" lengthAdjust="spacingAndGlyphs">044 555 0142</text>
    <text class="website" x="383" y="1008" font-size="40" text-anchor="middle" textLength="424" lengthAdjust="spacingAndGlyphs">www.briskcurrent.com</text>
  </svg>
</main>
</body>
</html>
```